Custom Wordpress Theme - Original and Professional

We are a boutique IT consulting firm that provide small and medium business in Australia three different levels of IT service.
We are looking for a developer who will create a customised, original and professional wordpress theme. We are looking for the developer to create a professional, clean, clear and simple theme with a stylish layout, images and icons.
Our three services are: IT support | IT Services | IT Solutions and we would like to clearly differentiate the difference in each level of service in as few words as possible.
IT Support is the ad hock “call us, when you need us” service, that smaller business or those with minimal issues use.
IT service is the unlimited service, that business with existing (and well maintained) IT systems choose and is both flexible and scalable including no contracts or paperwork required.
IT solutions are the unlimited service that businesses that need new or updated infrastructure choose and it includes all the hardware, software and services with no contracts or any ongoing commitment.
The main page on the web site will attract the visitor to choose the right “service level” for their business and then we will have a dedicated page for each service and another page for a comparison (table) to compare all three services.
Lastly we will need a contact us page that has both office locations (Sydney and Melbourne), contact phone numbers and an email form.
Items we are focused on for this project are: 1. Images, 2.Icons 3. Layout.
In summary we are looking for a custom WordPress theme into a 6 page (Home, IT Support, IT Services, IT Solutions, Compare Service levels and Contact us) website. The design must include relevant images and icons and be clear, simple, professional and sleek.

Thank you for your time and creativity and I look forward to working with you!

Target Market(s)

Small and Medium businesses in Australia

Industry/Entity Type

Boutique

Requirements
Must have
• - 6 Pages layout: Home, IT support, IT services, IT Solutions, Compare service levels and Contact us
- Images, Layout and Icons.
- Clean, Clear, Simple, Elegant, Stylish.
Nice to have
• - Some text (if possible but not required).
Should not have
• - Complexity.
- Confusing layout.
- Generic non matching images and icons.

```html
<!DOCTYPE html>
<html lang="en">
<head>
<meta charset="utf-8">
<title>Boutique – IT Services</title>
<link href="https://fonts.googleapis.com/css2?family=Source+Sans+3:wght@300;400;600&display=swap" rel="stylesheet">
<style>
  :root {
    --header-top: #0d3a80;
    --header-bottom: #061d4a;
    --white: #ffffff;
    --heading-blue: #1b3770;
    --body-text: #7a7a7a;
    --accent-orange: #f0872a;
    --rule: #e6e6e6;
    --panel-border: #d9d9d9;
    --footer-bg: #f7f7f7;
    --footer-text: #555555;
    --social: #5a5a5a;
  }
  * { box-sizing: border-box; margin: 0; padding: 0; }
  html, body { width: 1200px; height: 999px; overflow: hidden; }
  body {
    position: relative;
    background: var(--white);
    font-family: "Source Sans 3", "Myriad Pro", sans-serif;
    color: var(--body-text);
  }

  /* Header */
  .site-header {
    position: absolute; left: 0; top: 0; width: 1200px; height: 115px;
    background: linear-gradient(180deg, var(--header-top), var(--header-bottom));
  }
  .brand {
    position: absolute; left: 90px; top: 30px;
    font-size: 42px; font-weight: 400; color: var(--white); letter-spacing: 0.2px;
  }
  .phone {
    position: absolute; right: 88px; top: 11px;
    display: flex; align-items: center; gap: 4px;
    font-size: 23px; color: var(--white);
  }
  .phone svg { width: 20px; height: 22px; }
  .main-nav {
    position: absolute; right: 84px; top: 63px;
    display: flex; list-style: none;
  }
  .main-nav li {
    font-size: 19px; color: var(--white);
    padding: 0 13px; border-left: 1px solid rgba(255,255,255,0.35);
    line-height: 22px;
  }
  .main-nav li:first-child { border-left: none; }
  .main-nav li:last-child { padding-right: 0; }

  /* Hero */
  .hero {
    position: absolute; left: 82px; top: 115px; width: 1033px; height: 257px;
    background:
      radial-gradient(ellipse at 48% 40%, #f2f7fb 0%, #cfe0ee 22%, rgba(90,140,190,0) 55%),
      linear-gradient(90deg, #4a7fb0 0%, #1e5c9c 20%, #5b8ec0 45%, #2b6aa8 75%, #123f73 100%);
  }
  .hero-caption { position: absolute; left: 50px; top: 130px; color: var(--white); }
  .hero-title { font-size: 33px; font-weight: 400; line-height: 36px; }
  .hero-subtitle { font-size: 21px; font-weight: 400; line-height: 26px; }
  .hero-rule {
    position: absolute; left: 0; top: 372px; width: 1200px; height: 1px; background: var(--rule);
  }

  /* Main content */
  .content { position: absolute; left: 99px; top: 404px; width: 690px; }
  .content h1 {
    font-size: 29px; font-weight: 400; color: var(--heading-blue); line-height: 36px;
  }
  .team-photo {
    width: 409px; height: 156px; margin: 6px 0 10px -1px; border-radius: 4px;
    background: linear-gradient(100deg, #e8edf2 0%, #c9d3dc 35%, #f1f3f5 60%, #b8c3cd 100%);
  }
  .content p {
    font-size: 14.2px; font-weight: 300; line-height: 22.5px; margin-bottom: 8px; color: var(--body-text);
  }

  /* Sidebar */
  .services-panel {
    position: absolute; left: 815px; top: 390px; width: 315px; height: 375px;
    border: 1px solid var(--panel-border); border-radius: 9px; padding: 22px 38px 0 31px;
  }
  .services-panel h2 {
    font-size: 29px; font-weight: 400; color: var(--accent-orange); line-height: 36px; margin-bottom: 14px;
  }
  .service-list { list-style: none; margin-left: 3px; }
  .service-list li {
    display: flex; align-items: center; gap: 9px;
    height: 32.5px; font-size: 14.2px; font-weight: 300; color: #666;
    border-bottom: 1px solid #ececec;
  }
  .service-list li:last-child { border-bottom: none; }
  .service-list svg { width: 16px; height: 16px; flex: none; }

  /* Footer */
  .site-footer {
    position: absolute; left: 0; top: 870px; width: 1200px; height: 129px;
    background: var(--footer-bg); border-top: 1px solid #ececec;
  }
  .footer-nav {
    position: absolute; left: 80px; top: 42px; display: flex; list-style: none;
  }
  .footer-nav li {
    font-size: 17px; color: var(--footer-text); padding: 0 11px; line-height: 18px;
    border-left: 1px solid var(--footer-text);
  }
  .footer-nav li:first-child { border-left: none; padding-left: 0; }
  .copyright {
    position: absolute; left: 80px; top: 79px; font-size: 12.5px; color: var(--footer-text); font-weight: 300;
  }
  .social { position: absolute; left: 964px; top: 58px; display: flex; gap: 5px; }
  .social span {
    width: 32px; height: 32px; border-radius: 50%; background: var(--social); display: block;
  }
</style>
</head>
<body>

<header class="site-header">
  <div class="brand">Boutique</div>
  <div class="phone">
    <svg viewBox="0 0 20 22" aria-hidden="true">
      <path d="M4 1 L8 1 L9 6 L6.5 8 C8 12 10 14.5 13 16 L15 13.5 L19.5 15 L19.5 19 C19.5 20.5 18 21.5 16 21 C8 19 2 12 1 4.5 C0.8 2.5 2 1 4 1 Z" fill="#ffffff"/>
    </svg>
    <span>555.0142.7730</span>
  </div>
  <ul class="main-nav">
    <li>Home</li>
    <li>IT support</li>
    <li>IT services</li>
    <li>IT Solutions</li>
    <li>Compare service levels</li>
    <li>Contact us</li>
  </ul>
</header>

<section class="hero" role="img" aria-label="Data centre aisle with two hands passing a network cable between server racks">
  <div class="hero-caption">
    <div class="hero-title">IT Services</div>
    <div class="hero-subtitle">Donec scelerisque leo risus</div>
  </div>
</section>
<div class="hero-rule"></div>

<main class="content">
  <h1>IT Services</h1>
  <div class="team-photo" role="img" aria-label="Support team wearing headsets working at computers in a bright office"></div>
  <p>Nunc tempus felis vitae urna. Vivamus porttitor, g, purus nisi eleifend libero, a tempus libero lectus feugiat felis. Morbi diam mauris, viverra in, gravida eu, mattis in, ante. Morbi eget arcu.</p>
  <p>Phasellus felis dolor, scelerisque a, tempus eget, lobortis id, libero. Donec scelerisque leo ac risus. Praesent sit amet est. In dictum, dolor eu dictum porttitor, enim felis viverra mi eget luctus massa purus quis odio.</p>
  <p>Phasellus felis dolor, scelerisque a, tempus eget, lobortis id, libero. Donec scelerisque leo ac risus. Praesent sit amet est. In dictum, dolor eu dictum porttitor, enim felis viverra mi, eget luctus massa purus quis odio. Etiam nulla massa, pharetra facilisis, volutpat in, imperdiet sit amet, sem. Aliquam nec erat at purus cursus interdum. Vestibulum ligula augue, bibendum accumsan, vestibulum ut, commodo a, mi. Morbi ornare gravida elit. Inte-ger congue, augue et malesuada iaculis, ipsum dui aliquet felis, at cursus magna nisl nec elit</p>
</main>

<aside class="services-panel">
  <h2>Services We Provide</h2>
  <ul class="service-list">
    <li><svg viewBox="0 0 16 16" aria-hidden="true"><path d="M1 8.5 L4 6.5 L6.5 10 L13.5 1.5 L15.5 3 L7 14.5 Z" fill="#f0872a"/></svg>Morbi magna magna</li>
    <li><svg viewBox="0 0 16 16" aria-hidden="true"><path d="M1 8.5 L4 6.5 L6.5 10 L13.5 1.5 L15.5 3 L7 14.5 Z" fill="#f0872a"/></svg>Tincidunt a mattis non imperdiet</li>
    <li><svg viewBox="0 0 16 16" aria-hidden="true"><path d="M1 8.5 L4 6.5 L6.5 10 L13.5 1.5 L15.5 3 L7 14.5 Z" fill="#f0872a"/></svg>Sed odio est auctor ac</li>
    <li><svg viewBox="0 0 16 16" aria-hidden="true"><path d="M1 8.5 L4 6.5 L6.5 10 L13.5 1.5 L15.5 3 L7 14.5 Z" fill="#f0872a"/></svg>Sollicitudin in consequat vitae</li>
    <li><svg viewBox="0 0 16 16" aria-hidden="true"><path d="M1 8.5 L4 6.5 L6.5 10 L13.5 1.5 L15.5 3 L7 14.5 Z" fill="#f0872a"/></svg>Morbi magna magna</li>
    <li><svg viewBox="0 0 16 16" aria-hidden="true"><path d="M1 8.5 L4 6.5 L6.5 10 L13.5 1.5 L15.5 3 L7 14.5 Z" fill="#f0872a"/></svg>Tincidunt a mattis non imperdiet</li>
    <li><svg viewBox="0 0 16 16" aria-hidden="true"><path d="M1 8.5 L4 6.5 L6.5 10 L13.5 1.5 L15.5 3 L7 14.5 Z" fill="#f0872a"/></svg>Sed odio est auctor ac</li>
    <li><svg viewBox="0 0 16 16" aria-hidden="true"><path d="M1 8.5 L4 6.5 L6.5 10 L13.5 1.5 L15.5 3 L7 14.5 Z" fill="#f0872a"/></svg>Sollicitudin in consequat vitae</li>
  </ul>
</aside>

<footer class="site-footer">
  <ul class="footer-nav">
    <li>Home</li>
    <li>IT support</li>
    <li>IT services</li>
    <li>IT Solutions</li>
    <li>Compare service levels</li>
    <li>Contact us</li>
  </ul>
  <div class="copyright">Copyright © 2013 Company Name.&nbsp; All right reserved</div>
  <div class="social" aria-label="Social links">
    <span></span><span></span><span></span><span></span>
  </div>
</footer>

</body>
</html>
```